Song Cover Art. Song Tittle Lift The Floor

I would like a design for my songs. I'm a producer and i prouder EDM music such as Big Room House / Electro House music. Currently i have a new songs tittle name Lift The Floor and i need a cover art for my songs. I'm not sure what design i have in mind right now and i would like someone to create it for me. My DJ name is DJ Vex.
Reason: Hey, i will give sometimes for you guys to create the design for me. Please do zorvix edm cover art or brenlow - lift the floor.
Target Market(s)
Electronic Dance Music Lovers
Industry/Entity Type
House
Look and feel
Each slider illustrates characteristics of the customer's brand and the style your logo design should communicate.

```html
<!DOCTYPE html>
<html lang="en">
<head>
<meta charset="utf-8">
<title>Lift The Floor – DJ Vex</title>
<link rel="stylesheet" href="https://fonts.googleapis.com/css2?family=Oswald:wght@500&display=swap">
<style>
  :root {
    --page-bg: #ffffff;
    --cover-bg: #050403;
    --text-light: #ffffff;
    --ember-bright: #e07a1c;
    --ember-mid: #8a3a0c;
    --ember-deep: #2a1004;
  }
  html, body {
    margin: 0;
    padding: 0;
    width: 1200px;
    height: 900px;
    overflow: hidden;
    background: var(--page-bg);
  }
  .cover {
    position: absolute;
    left: 190px;
    top: 40px;
    width: 820px;
    height: 820px;
    background: var(--cover-bg);
    overflow: hidden;
    font-family: "Oswald", "Arial Narrow", sans-serif;
    color: var(--text-light);
  }
  .song-title {
    position: absolute;
    left: 22px;
    top: 12px;
    margin: 0;
    font-weight: 500;
    font-size: 80px;
    line-height: 1.2;
    letter-spacing: -1px;
    text-transform: uppercase;
  }
  .artist-name {
    position: absolute;
    right: 60px;
    bottom: 26px;
    margin: 0;
    font-weight: 500;
    font-size: 54px;
    line-height: 1.2;
    letter-spacing: -0.5px;
    text-transform: uppercase;
  }
  .ember-spiral {
    position: absolute;
    left: 138px;
    top: 148px;
    width: 560px;
    height: 560px;
    border-radius: 50%;
    background: radial-gradient(circle at 50% 45%,
      var(--ember-bright) 0%,
      var(--ember-mid) 45%,
      var(--ember-deep) 85%,
      var(--cover-bg) 100%);
  }
</style>
</head>
<body>
  <main class="cover">
    <h1 class="song-title">Lift The Floor</h1>
    <div class="ember-spiral" role="img" aria-label="Glowing ember-textured spiral vortex in orange and black"></div>
    <p class="artist-name">DJ Vex</p>
  </main>
</body>
</html>
```